Pilates trainer needs new website

Summary: I need a new, meaningful website in a 1-page format, but one that can be expanded if necessary. I teach in various studios and in the future also in companies. Therefore, the website should convey growth, joy, uniqueness, workout and a bit of luxury.
The website should be inviting.
Layout:
Introduction what I offer
A bit about me
Option to upload price list and timetable in PDF format
Studio address where I teach
The color scheme should be petrol, gold, and colors that match. Not too dark, please.
My current website www.pilates-wendmarau.de, new domain is pilates-corvanel.com (I have already purchased it)
Logo file attached
I have attached a few suggestions but I am also happy to be surprised.

Target Market(s)

Pilates private and small groups,

Industry/Entity Type

Pilates teacher freelancer

Coding

Coded - Design and coding required

Number of Pages Required

1 page

Requirements
Must have
• Welcoming appearance, about me, pictures, offers, colors from the logo but don't get do dark, more fresh and a bit luxurious
Should not have
• Not too wild and going crazy with colors

```html
<!DOCTYPE html>
<html lang="de">
<head>
<meta charset="utf-8">
<title>Pilates Corvanel – Marlene Vossberg</title>
<link href="https://fonts.googleapis.com/css2?family=Cinzel:wght@500;600;700&family=Pinyon+Script&family=Montserrat:wght@400;500;600&display=swap" rel="stylesheet">
<style>
:root{
  --teal:#19a797;
  --teal-dark:#12897c;
  --mint:#eef7f5;
  --mint-2:#d7efea;
  --ink:#1c1c1c;
  --text:#3a3a3a;
  --muted:#8a8a8a;
  --white:#ffffff;
}
*{margin:0;padding:0;box-sizing:border-box}
html,body{width:1200px;height:4494px;overflow:hidden}
body{position:relative;background:var(--white);font-family:"Montserrat",sans-serif;color:var(--text)}
.abs{position:absolute}
.caps{font-family:"Cinzel",serif;font-variant:small-caps;letter-spacing:2px;color:var(--ink)}
.script{font-family:"Pinyon Script",cursive;color:var(--teal);font-size:46px;line-height:1}
.btn{position:absolute;display:flex;align-items:center;justify-content:center;gap:10px;background:var(--teal);color:var(--white);border-radius:30px;font-family:"Cinzel",serif;font-size:14px;letter-spacing:1.5px;font-weight:600}
.center{left:0;width:1200px;text-align:center}
.brand{display:flex;align-items:center;gap:8px;font-family:"Montserrat",sans-serif;font-weight:600;color:var(--teal)}
.brand-dot{width:18px;height:18px;border-radius:50%;background:var(--teal)}
/* header */
.site-nav{top:22px;left:368px;display:flex;gap:32px}
.site-nav a{font-family:"Cinzel",serif;font-size:12px;font-weight:600;color:var(--ink);text-decoration:none;letter-spacing:1px}
.hero-title{left:138px;top:172px;font-size:40px;line-height:46px;font-weight:700;letter-spacing:3px}
.hero-sub{left:138px;top:322px;font-size:20px;color:var(--ink)}
.hero-visual{left:560px;top:0;width:640px;height:530px;background:radial-gradient(circle at 58% 45%,#19a797 0 28%,#bfe5df 42%,#ffffff 70%)}
/* welcome */
.welcome p{font-size:12px;line-height:22px;color:var(--ink)}
/* about band */
.band{left:0;width:1200px}
.photo{position:absolute;background:linear-gradient(160deg,#e9e2d6,#c9b79a 60%,#3b3b4a)}
.about-text{left:780px;font-size:12px;line-height:22px;color:var(--ink)}
/* services */
.card{position:absolute;top:1840px;width:300px;height:345px;padding:32px 30px}
.card.featured{background:var(--white);box-shadow:0 10px 30px rgba(0,0,0,.08)}
.card .icon{width:62px;height:62px;border-radius:50%;background:var(--mint-2);position:relative}
.card h3{margin-top:22px;font-family:"Cinzel",serif;font-size:17px;font-weight:600;letter-spacing:1.5px;line-height:22px;color:var(--ink)}
.card p{margin-top:24px;font-size:12px;line-height:22px;color:var(--ink)}
.plus{margin-top:30px;width:22px;height:22px;border-radius:50%;border:1px solid var(--mint-2);color:var(--teal);display:flex;align-items:center;justify-content:center;font-size:14px}
/* locations */
.loc-item{position:absolute;left:138px;display:flex;gap:20px;align-items:center}
.loc-icon{width:50px;height:50px;border-radius:50%;border:1px solid var(--mint-2);display:flex;align-items:center;justify-content:center;background:var(--white)}
.loc-item h4{font-family:"Cinzel",serif;font-size:13px;font-weight:600;letter-spacing:1.5px;color:var(--ink)}
.loc-item p{font-size:14px;line-height:19px;color:var(--ink)}
.map{left:600px;top:2478px;width:455px;height:377px;border:8px solid var(--white);box-shadow:0 6px 20px rgba(0,0,0,.06);background:linear-gradient(135deg,#d5efe3,#bfe3d3 55%,#cfe9f0)}
/* testimonial */
.quote-box{left:232px;top:3205px;width:726px;height:262px;background:var(--mint);text-align:center;padding-top:70px}
.quote-box h4{font-family:"Cinzel",serif;font-size:15px;color:var(--teal);letter-spacing:2px;font-weight:600}
.quote-box .role{font-size:14px;color:var(--ink);margin-top:10px}
.quote-box p{font-size:12px;line-height:22px;color:var(--muted);margin:22px 60px 0}
.quote-mark{font-family:"Cinzel",serif;font-size:150px;font-weight:700;color:var(--teal);line-height:1}
.avatar{left:553px;top:3155px;width:84px;height:84px;border-radius:50%;border:4px solid var(--white);background:linear-gradient(160deg,#c9a58a,#5a3c30);box-shadow:0 4px 12px rgba(0,0,0,.1)}
.arrow{width:32px;height:32px;border-radius:50%;border:1px solid #cfcfcf;display:flex;align-items:center;justify-content:center;color:#777;font-size:14px;background:var(--white)}
.dots{top:3552px;left:548px;display:flex;gap:7px}
.dots span{width:9px;height:9px;border-radius:50%;background:#cfd9d7}
.dots span.on{background:var(--teal)}
/* form */
.field{position:absolute;width:270px;border-bottom:1px solid #d7d7d7;height:52px}
.field label{display:block;font-size:10px;color:var(--muted)}
.field span{display:block;margin-top:14px;font-size:11px;color:var(--ink)}
.field svg{position:absolute;right:6px;top:22px}
/* footer */
.footer{left:0;top:4213px;width:1200px;height:281px;background:var(--teal)}
.footer-logo{left:535px;top:4170px;width:130px;height:130px;border-radius:50%;background:var(--teal);display:flex;align-items:center;justify-content:center}
.footer-nav{top:4342px;left:0;width:1200px;display:flex;justify-content:center;gap:40px;font-family:"Cinzel",serif;font-size:12px;font-weight:600;letter-spacing:1px;color:var(--white)}
.social{top:4382px;left:547px;display:flex;gap:8px}
.social span{width:28px;height:28px;border-radius:50%;border:1.5px solid var(--white)}
.footer-bottom{top:4450px;left:138px;width:918px;border-top:1px solid rgba(255,255,255,.3);padding-top:14px;display:flex;justify-content:space-between;font-size:12px;color:var(--white)}
</style>
</head>
<body>

<!-- Header -->
<div class="abs brand" style="left:138px;top:50px;font-size:18px"><span class="brand-dot"></span>Pilates Corvanel</div>
<nav class="abs site-nav">
  <a href="#">Über Uns</a><a href="#">Dienstleistungen</a><a href="#">Standorte</a><a href="#">Kontaktiere Uns</a>
</nav>

<!-- Hero -->
<div class="abs hero-visual" role="img" aria-label="Trainerin in einer Pilates-Dehnposition vor einem türkisen Kreis"></div>
<h1 class="abs caps hero-title">Entdecken Sie<br>die Freude am<br>Pilates</h1>
<p class="abs hero-sub">Marlene Vossberg Pilates Studio Trainerin</p>
<a class="btn" style="left:138px;top:375px;width:212px;height:44px">Kontaktiere Uns</a>

<!-- Welcome -->
<section class="welcome">
  <h2 class="abs caps center" style="top:600px;font-size:18px;font-weight:600">Willkommen Zu</h2>
  <div class="abs script center" style="top:628px">Pilates Corvanel</div>
  <div class="abs" style="left:205px;top:690px;width:790px;text-align:center">
    <p>Möchten Sie Ihre Kraft, Flexibilität und Ihr allgemeines Wohlbefinden durch Pilates-Training verbessern? Dann sind Sie bei Pilates Corvanel genau richtig. Wir sind auf Pilates-Training für private Sitzungen und kleine Gruppen spezialisiert und bieten ein einzigartiges und luxuriöses Trainingserlebnis.</p>
    <p style="margin-top:12px">Unsere erfahrenen Dozenten unterrichten in verschiedenen Studios und stehen auch für zukünftige Kurse in Unternehmen zur Verfügung. Wir sind bestrebt, in unseren Schulungen Wachstum, Freude und einen Hauch von Luxus zu vermitteln.</p>
  </div>
  <a class="btn" style="left:520px;top:830px;width:156px;height:42px">Mehr Lesen</a>
</section>

<!-- About band -->
<svg class="abs band" style="top:950px" width="1200" height="710" viewBox="0 0 1200 710">
  <path d="M0 20 C300 -10 600 60 1200 5 L1200 690 C900 650 500 720 0 680 Z" fill="#eef7f5"/>
  <circle cx="250" cy="166" r="97" fill="none" stroke="#19a797" stroke-width="1.2"/>
  <path d="M405 35 C360 90 360 200 420 260" fill="none" stroke="#19a797" stroke-width="1.2"/>
  <path d="M0 555 C60 560 80 470 140 450 C200 430 260 450 300 420" fill="none" stroke="#19a797" stroke-width="1.2"/>
</svg>
<div class="photo" style="left:138px;top:1235px;width:245px;height:243px" role="img" aria-label="Trainerin bei einer Übung am Pilates-Gerät"></div>
<div class="photo" style="left:430px;top:1100px;width:302px;height:457px" role="img" aria-label="Trainerin sitzend auf einem Pilates-Stuhl im Studio"></div>
<h2 class="abs caps" style="left:780px;top:1148px;font-size:18px;font-weight:600">Über Mich</h2>
<div class="abs script" style="left:780px;top:1175px">Marlene Vossberg</div>
<p class="abs" style="left:780px;top:1235px;font-size:14px;color:var(--ink);font-weight:500">Pilates Studio- und Mattentrainerin</p>
<p class="abs about-text" style="top:1268px;width:275px">Meine Liebe zum Pilates habe ich vor mehreren Jahren entdeckt und ziemlich schnell hatte ich den Wunsch diese Methode unterrichten zu wollen und so viel Menschen wie möglich von den positiven Auswirkungen zu überzeugen. Meine Ausbildung zur Pilates Mattentrainerin habe ich bei Balance Flow Akademie sehr erfolgreich abgeschlossen.</p>
<a class="btn" style="left:780px;top:1468px;width:156px;height:40px">Mehr Lesen</a>

<!-- Services -->
<h2 class="abs caps center" style="top:1724px;font-size:18px;font-weight:600">Dienstleistungen</h2>
<div class="abs script center" style="top:1752px">Unsere Dienstleistungen</div>

<div class="card" style="left:133px">
  <div class="icon" role="img" aria-label="Symbol Einzeltraining"></div>
  <h3>Private<br>Sessions</h3>
  <p>Ut enim ad minim veniam qui nostrud exercitation ullamco laboris ni aliquip ex ea commodo consequat.</p>
</div>
<div class="card featured" style="left:445px">
  <div class="icon" role="img" aria-label="Symbol Gruppentraining"></div>
  <h3>Kleine Gruppe<br>Klassen</h3>
  <p>Ut enim ad minim veniam qui nostrud exercitation ullamco laboris ni aliquip ex ea commodo consequat.</p>
  <div class="plus">+</div>
</div>
<div class="card" style="left:778px">
  <div class="icon" role="img" aria-label="Symbol Firmentraining"></div>
  <h3>Unternehmen<br>Ausbildung</h3>
  <p>Ut enim ad minim veniam qui nostrud exercitation ullamco laboris ni aliquip ex ea commodo consequat.</p>
</div>
<a class="btn" style="left:438px;top:2223px;width:320px;height:42px">
  <svg width="20" height="18" viewBox="0 0 20 18"><rect x="1" y="2" width="18" height="15" rx="2" fill="none" stroke="#fff" stroke-width="1.4"/><path d="M1 7h18M6 0v4M14 0v4" stroke="#fff" stroke-width="1.4"/></svg>
  Preisliste und Fahrplan
</a>

<!-- Locations band -->
<svg class="abs band" style="top:2375px" width="1200" height="610" viewBox="0 0 1200 610">
  <path d="M0 10 C350 -10 700 40 1200 0 L1200 595 C850 560 450 610 0 590 Z" fill="#eef7f5"/>
</svg>
<h2 class="abs caps" style="left:138px;top:2503px;font-size:18px;font-weight:600">Standorte</h2>
<div class="abs script" style="left:138px;top:2532px">Studiostandorte</div>
<div class="loc-item" style="top:2612px">
  <div class="loc-icon"><svg width="16" height="22" viewBox="0 0 16 22"><path d="M8 1a7 7 0 0 0-7 7c0 5 7 13 7 13s7-8 7-13a7 7 0 0 0-7-7z" fill="none" stroke="#19a797" stroke-width="1.8"/><circle cx="8" cy="8" r="2.5" fill="#19a797"/></svg></div>
  <div><h4>Adresse</h4><p>Lindenhofweg 4 83712 Oberaltbach<br>Eingang um die Ecke 2.OG</p></div>
</div>
<div class="loc-item" style="top:2698px">
  <div class="loc-icon"><svg width="20" height="20" viewBox="0 0 24 24"><path d="M6.6 10.8a15 15 0 0 0 6.6 6.6l2.2-2.2c.3-.3.7-.4 1-.2 1.1.4 2.3.6 3.6.6.6 0 1 .4 1 1V20c0 .6-.4 1-1 1A17 17 0 0 1 3 4c0-.6.4-1 1-1h3.5c.6 0 1 .4 1 1 0 1.3.2 2.5.6 3.6.1.3 0 .7-.2 1z" fill="#19a797"/></svg></div>
  <div><h4>Telefon</h4><p>+49 151 2046 8813</p></div>
</div>
<div class="loc-item" style="top:2778px">
  <div class="loc-icon"><svg width="20" height="16" viewBox="0 0 20 16"><rect x="1" y="1" width="18" height="14" rx="2" fill="none" stroke="#19a797" stroke-width="1.8"/><path d="M1 2l9 7 9-7" fill="none" stroke="#19a797" stroke-width="1.8"/></svg></div>
  <div><h4>Email</h4><p>info@pilates-wendmarau.de</p></div>
</div>
<div class="abs map" role="img" aria-label="Karte mit der Lage des Studios"></div>

<!-- Testimonials -->
<h2 class="abs caps center" style="top:3048px;font-size:18px;font-weight:600">Referenzen</h2>
<div class="abs script center" style="top:3076px">Zufriedene Kunden</div>
<div class="abs quote-box">
  <h4>Clara Wendt</h4>
  <div class="role">Lorem Ipsum</div>
  <p>Ut enim ad minim veniam, quis nostrud exercitation ullamco laboris nisi ut aliquip ea commodo consequat. Duis aute irure dolor in reprehenderit in voluptate velit esse cillum dolore eu fugiat nulla pariatur. Excepteur sint occaecat cupidatat non proident, sunt in culpa qui officia deserunt mollitest laborum.</p>
</div>
<div class="abs quote-mark" style="left:236px;top:3150px">“</div>
<div class="abs quote-mark" style="left:870px;top:3440px">”</div>
<div class="abs avatar" role="img" aria-label="Porträt einer Kundin"></div>
<div class="abs arrow" style="left:158px;top:3321px">‹</div>
<div class="abs arrow" style="left:1004px;top:3321px">›</div>
<div class="abs dots"><span></span><span class="on"></span><span></span><span></span><span></span><span></span></div>

<!-- Contact -->
<h2 class="abs caps center" style="top:3645px;font-size:18px;font-weight:600">Kontaktiere Uns</h2>
<div class="abs script center" style="top:3673px">Schnelle Anfragen</div>
<div class="field" style="left:308px;top:3752px"><label>Vorname</label><span>Michael</span>
  <svg width="16" height="16" viewBox="0 0 16 16"><circle cx="8" cy="5" r="3.5" fill="none" stroke="#999"/><path d="M1.5 15c0-4 13-4 13 0z" fill="none" stroke="#999"/></svg></div>
<div class="field" style="left:612px;top:3752px"><label>Familienname</label><span>Smith</span>
  <svg width="16" height="16" viewBox="0 0 16 16"><circle cx="8" cy="5" r="3.5" fill="none" stroke="#999"/><path d="M1.5 15c0-4 13-4 13 0z" fill="none" stroke="#999"/></svg></div>
<div class="field" style="left:308px;top:3832px"><label>Telefon</label><span>123 456 7890</span>
  <svg width="16" height="16" viewBox="0 0 24 24"><path d="M6.6 10.8a15 15 0 0 0 6.6 6.6l2.2-2.2c.3-.3.7-.4 1-.2 1.1.4 2.3.6 3.6.6.6 0 1 .4 1 1V20c0 .6-.4 1-1 1A17 17 0 0 1 3 4c0-.6.4-1 1-1h3.5c.6 0 1 .4 1 1 0 1.3.2 2.5.6 3.6.1.3 0 .7-.2 1z" fill="none" stroke="#999" stroke-width="1.4"/></svg></div>
<div class="field" style="left:612px;top:3832px"><label>Email</label><span>info@mailbeispiel.de</span>
  <svg width="18" height="14" viewBox="0 0 20 16"><rect x="1" y="1" width="18" height="14" rx="2" fill="none" stroke="#999"/><path d="M1 2l9 7 9-7" fill="none" stroke="#999"/></svg></div>
<div class="field" style="left:308px;top:3912px;width:574px;height:98px"><label>Nachricht</label><span>Geben Sie Ihre Nachricht ein</span>
  <svg width="18" height="16" viewBox="0 0 20 16"><ellipse cx="9" cy="7" rx="8" ry="5.5" fill="none" stroke="#999"/><path d="M4 11l-2 4 5-3" fill="none" stroke="#999"/></svg></div>
<a class="btn" style="left:498px;top:4050px;width:200px;height:42px">Jetzt Absenden</a>

<!-- Footer -->
<footer>
  <div class="abs footer"></div>
  <div class="abs footer-logo"><div class="brand" style="color:var(--white);font-size:14px;flex-direction:column;gap:6px"><span class="brand-dot" style="background:var(--white)"></span>Pilates Corvanel</div></div>
  <nav class="abs footer-nav"><span>Über Uns</span><span>/</span><span>Dienstleistungen</span><span>/</span><span>Standorte</span><span>/</span><span>Kontaktiere Uns</span></nav>
  <div class="abs social" aria-label="Soziale Netzwerke"><span></span><span></span><span></span></div>
  <div class="abs footer-bottom"><span>© 2024 Pilates Corvanel. Alle Rechte vorbehalten.</span><span>Haftungsausschluss</span></div>
</footer>

</body>
</html>
```